Wordpress Design Project

WHO WE ARE:
Bright Path Web Growth is not just another SEO or PPC company. We work with our clients to help them grow their business and achieve their goals. Our commitment to doing what is best for the customer, is why we have grown so quickly. We believe our business is not about advertising BUT about connecting customers & growing our clients businesses. We see our product as helping people, not selling a product.

PROJECT OVERVIEW:
I need to create a wordpress website for my business, www.brightpathwebgrowth.com.au

I need a whole new site created showing all of my services. The services include:
NOTE: These are not the main focus of the home page.

Consulting & Strategy Planning
Search Engine Optimisation
Pay Per Click
Re-Marketing

Once I have selected the top home page design, I will need a product and blog page designed.

SITE DESIGN:
If I was to explain the kind of style I am looking for, it would be high-street, New York agency look, web 2.0. Clean, elegant, stylish, high quality and simple looking. Kind of like you would expect from an quince website.

Think of car advertising, the closest to the target market & look/feel Im looking for would be Ravenmotor, Korel, Tamar, Brandin, Zepra.

However, I am open to any design style.

DO NOT let this restrict your creativity BUT here are some websites I like the look of.

Home page:
http://www.layoutfoundry.example/demo/52816.html
https://www.vantorix.example/intl/en/halo/devices/
http://www.vantorix.example/intl/en/halo/devices/features-different.html
http://www.layoutfoundry.example/demo/47190.html
https://www.vantorix.example/intl/en/halo/browser/features.html

Product Page:
http://www.vantorix.example/intl/en/halo/devices/buynow.html#instore

NOTE: I just added a file called "I like this color scheme.png" you can play around with something like this as well.
Updates

Please do not use the content from my current website. That is for a PPC service, the new site is for an full service agency.

Also, the message/tagline is the feature or most prominent element of the website..... Not the services we offer, these are secondary.

Great designs so far everyone, but I think I'm looking a little simpler and less crowded.  Closer to the sample sites I sent.... keep em coming.

Also, I would prefer that the 4 services, do not visually over power the tag line.  The 4 services are not important to the home page.

Lets make this easy, since every design I receive is almost the same...

Make the design look something like these 2 websites.
https://www.vantorix.example/intl/en/halo/browser/features.html#simplicity

Target Market(s)

Business Owners and entreprenuers who are well established, typically in the 35-60 year old range and spend 100k-1m in advertising per year. They big brands that target these people are Ravenmotor, Korel, Tamar, Brandin, Zepra, this should give you the feel for what I am after.

Industry/Entity Type

Advertising

Requirements
Must have
• 1. Navigations: Home, Services, About Us, Blog, Contact Us

2. The main home page words should be.... "We Grow Your Business Online" and "Clear Aim, Clear Plan, Clear Team, Bright Path Web Growth" (should use logo for last one)
I would like to see this tagline somewhere in the site "We Don't Want to be the Biggest, Just the Best!"

3. Product page must have a contact form with (name, email, phone, website)
This form must show an offer of "Free Strategy Sessions, Double your website leads", I have included an image to show as an example for the lead form "lead form example.png", see attached.

Nice to have
• I would like to see 1 or 2 of these idea's in the design.

1. I have attached some logos for Bidlane & Metricove certifications + Web association logo you can use for design purposes.

2. You can put company logo's in the design and I can change them to my clients logos at a later date.

3. Testimonials

4. Since our business is about people, pictures of people like business owners, customers using technology such as an slate, or anything like that would be good. However, is not necessary. Some idea: http://www.peerlattice.example/advertising
Should not have
• There will be no video on the design.

```html
<!DOCTYPE html>
<html lang="en">
<head>
<meta charset="utf-8">
<title>Bright Path Web Growth</title>
<link rel="stylesheet" href="https://fonts.googleapis.com/css2?family=Roboto+Slab:wght@300;400;500&family=Roboto:wght@400;700&display=swap">
<style>
  :root {
    --page: #121212;
    --hero: #1d1d1e;
    --panel: #1a1a1b;
    --white: #ffffff;
    --blue: #3d7fc6;
    --link: #6f9fd0;
    --nav: #6f8fb0;
    --bullet: #5d6d82;
    --tile-grey-top: #6a6a6a;
    --tile-grey-bottom: #3a3a3a;
    --tile-blue-top: #1f5a88;
    --tile-blue-bottom: #163149;
    --orange: #e0640e;
    --green: #2f8a55;
    --field: #e6e6e6;
    --placeholder: #9a9a9a;
  }
  * { box-sizing: border-box; margin: 0; padding: 0; }
  html, body { width: 1003px; height: 1200px; overflow: hidden; }
  body {
    background: var(--page);
    font-family: "Roboto Slab", serif;
    color: var(--white);
    position: relative;
  }
  .site-header { position: absolute; left: 0; top: 0; width: 1003px; height: 77px; background: #1a1a1a; }
  .brand { position: absolute; left: 124px; top: 22px; display: flex; align-items: center; gap: 10px; }
  .brand-dot { width: 30px; height: 30px; border-radius: 50%; background: var(--blue); }
  .brand-name { font-size: 24px; font-weight: 400; color: #e8e8e8; }
  .main-nav { position: absolute; left: 432px; top: 23px; display: flex; gap: 0; }
  .main-nav a { font-size: 17px; color: var(--nav); text-decoration: none; padding: 5px 16px; margin-right: 15px; }
  .main-nav a.active { color: var(--white); background: #2b2b2c; border-radius: 3px; }

  .hero { position: absolute; left: 0; top: 77px; width: 1003px; height: 283px; background: linear-gradient(#202021, #1a1a1b); }
  .hero-devices { position: absolute; left: 100px; top: 48px; width: 330px; height: 210px; border-radius: 6px;
    background: linear-gradient(160deg, #3a3632 0%, #6d665b 40%, #2a2826 100%); }
  .hero-copy { position: absolute; left: 498px; top: 78px; width: 440px; text-align: center; }
  .hero-title { font-weight: 400; font-size: 49px; line-height: 46px; }
  .hero-title .accent { display: block; color: var(--blue); font-size: 47px; }
  .hero-tagline { font-size: 16.5px; margin-top: 6px; letter-spacing: 0.2px; }

  .testimonial { position: absolute; left: 32px; top: 376px; width: 598px; height: 148px; background: var(--panel); padding: 14px 16px; }
  .testimonial h2 { font-size: 26px; font-weight: 400; }
  .quote-mark { position: absolute; right: 16px; top: 0; font-size: 90px; line-height: 90px; font-weight: 500; }
  .testimonial blockquote { font-size: 12.5px; line-height: 16px; margin-top: 10px; width: 490px; padding-left: 2px; }
  .testimonial cite { position: absolute; right: 42px; top: 102px; font-style: normal; text-align: left; }
  .testimonial cite .name { display: block; color: var(--link); font-size: 15px; }
  .testimonial cite .site { display: block; font-size: 9px; margin-top: 2px; }

  .services { position: absolute; left: 35px; top: 543px; }
  .service-tile { position: absolute; width: 290px; height: 133px; border-radius: 10px;
    background: linear-gradient(var(--tile-grey-top), var(--tile-grey-bottom)); display: flex; align-items: center; justify-content: center;
    font-size: 30px; line-height: 26px; color: var(--white); text-shadow: 0 2px 3px rgba(0,0,0,.5); }
  .service-tile.featured { background: linear-gradient(var(--tile-blue-top), var(--tile-blue-bottom)); }
  .service-tile .indent { padding-left: 36px; }
  .service-tile .pointer { position: absolute; left: 135px; bottom: 0; width: 0; height: 0;
    border-left: 10px solid transparent; border-right: 10px solid transparent; border-bottom: 13px solid #c5c5c5; }

  .lead-form { position: absolute; left: 38px; top: 844px; width: 590px; height: 222px; background: var(--panel); }
  .offer { position: absolute; left: 28px; top: 22px; }
  .offer-circle { position: absolute; left: 0; top: 0; width: 76px; height: 76px; border-radius: 50%; background: var(--green);
    border: 2px dashed #9fd2b2; display: flex; align-items: center; justify-content: center; font-size: 26px; z-index: 2; }
  .offer-arrow { position: absolute; left: 58px; top: 12px; }
  .offer-arrow span { position: absolute; left: 32px; width: 150px; text-align: center; color: #fff; font-family: "Roboto", sans-serif; }
  .offer-arrow .line1 { top: 8px; font-size: 11px; color: #fde2c6; }
  .offer-arrow .line2 { top: 20px; font-size: 18px; font-weight: 700; text-decoration: underline; }
  .guarantee { position: absolute; left: 52px; top: 130px; width: 185px; text-align: center; font-size: 15.5px; line-height: 18px; }
  .guarantee .brace { position: absolute; top: -2px; font-size: 44px; line-height: 48px; color: var(--orange); font-weight: 300; }
  .guarantee .brace.left { left: -6px; } .guarantee .brace.right { right: -6px; }
  .guarantee .hi { color: var(--link); font-family: "Roboto", sans-serif; }
  .guarantee .lo { color: var(--link); }
  .fields { position: absolute; left: 303px; top: 19px; display: flex; flex-direction: column; gap: 11px; }
  .fields input { width: 244px; height: 37px; border: 1px solid #bbb; border-radius: 2px;
    background: linear-gradient(#f2f2f2, #dcdcdc); font-family: "Roboto", sans-serif; font-size: 15px; padding-left: 12px; color: #444; }
  .fields input::placeholder { color: var(--placeholder); }

  .reasons { position: absolute; left: 660px; top: 376px; width: 308px; height: 690px; background: var(--panel); padding: 18px 14px 0 12px; }
  .reasons h3 { font-size: 19.5px; font-weight: 400; line-height: 19px; padding-left: 9px; }
  .reasons h3 span { display: block; padding-left: 120px; }
  .reasons ul { list-style: none; margin-top: 14px; }
  .reasons li { position: relative; padding-left: 29px; font-size: 14.3px; line-height: 18.5px; font-weight: 300; margin-bottom: 12px; }
  .reasons li::before { content: ""; position: absolute; left: 2px; top: 4px; width: 14px; height: 14px; border-radius: 50%; background: var(--bullet); }
  .reasons li strong { font-weight: 300; color: var(--link); }

  .site-footer { position: absolute; left: 37px; top: 1091px; width: 933px; height: 88px; background: var(--panel); }
  .footer-nav { position: absolute; left: 69px; top: 34px; font-size: 13.5px; color: var(--nav); }
  .footer-nav a { color: var(--nav); text-decoration: none; }
  .footer-nav a.active { color: var(--link); }
  .footer-nav .sep { margin: 0 8px; }
  .badge { position: absolute; background: #3a3a3b; }
  .badge.cert { left: 505px; top: 7px; width: 205px; height: 74px; border-radius: 4px; }
  .badge.assoc { left: 746px; top: 20px; width: 140px; height: 48px; border-radius: 24px; }
</style>
</head>
<body>
  <header class="site-header">
    <div class="brand"><span class="brand-dot"></span><span class="brand-name">Bright Path Web Growth</span></div>
    <nav class="main-nav">
      <a href="#" class="active">Home</a><a href="#">Services</a><a href="#">About Us</a><a href="#">Blog</a><a href="#">Contact Us</a>
    </nav>
  </header>

  <section class="hero">
    <div class="hero-devices" role="img" aria-label="Website shown on a desktop monitor, laptop, tablet and phone"></div>
    <div class="hero-copy">
      <h1 class="hero-title">We Grow Your <span class="accent">BUSINESS ONLINE</span></h1>
      <p class="hero-tagline">WE DON'T WANT TO BE THE BIGGEST, JUST THE BEST!</p>
    </div>
  </section>

  <section class="testimonial">
    <h2>WHAT PEOPLE SAY:</h2>
    <span class="quote-mark">”</span>
    <blockquote>„ MANAPSÁG, AMIKOR EGYRE TÖBB ÉS TÖBB INGATLANIRODA NYÍLIK, FONTOSNAK TARTOM, HOGY - NAPJAINK ELVÁRÁSAINAK MEGFELELVE - MINÉL TÖBB HELYEN LEGYEK MEGTALÁLHATÓ. A BRIGHT PATH WEB GROWTH ÁLTAL KÉSZÍTETT,...</blockquote>
    <cite><span class="name">LENA MARSH</span><span class="site">WWW.CRAFTHIVE.EXAMPLE</span></cite>
  </section>

  <section class="services">
    <div class="service-tile featured" style="left:0;top:0;"><div>Consulting &amp;<br><span class="indent">Strategy Planning</span></div><span class="pointer"></span></div>
    <div class="service-tile" style="left:306px;top:0;"><div>Search Engine<br><span class="indent" style="padding-left:62px">Optimisation</span></div></div>
    <div class="service-tile" style="left:0;top:148px;">Pay Per Click</div>
    <div class="service-tile" style="left:306px;top:148px;">Re-Marketing</div>
  </section>

  <section class="lead-form">
    <div class="offer">
      <div class="offer-circle">Free</div>
      <svg class="offer-arrow" width="232" height="48" viewBox="0 0 232 48" aria-hidden="true">
        <path d="M0 2 H200 L230 24 L200 46 H0 Z" fill="#e0640e"/>
      </svg>
      <div class="offer-arrow"><span class="line1">STRATEGY SESSION</span><span class="line2">HERE!</span></div>
    </div>
    <p class="guarantee">
      <span class="brace left">{</span><span class="brace right">}</span>
      A Guaranteed Way<br>to <span class="hi">Double Website</span><br><span class="hi">Conversion Rate</span>
    </p>
    <form class="fields">
      <input type="text" placeholder="Name:">
      <input type="email" placeholder="E-mail:">
      <input type="tel" placeholder="Phone number:">
      <input type="url" placeholder="Website:">
    </form>
  </section>

  <aside class="reasons">
    <h3>6 Reasons you need to <span>speak with us...</span></h3>
    <ul>
      <li><strong>Guaranteed Results:</strong> We guarantee to increase the return of your online advertising by 25%.</li>
      <li><strong>Huge Savings:</strong> Large Agencies have large overheads, as Independent Consultants our costs are minimal which means clients save to.</li>
      <li><strong>Independent Advise:</strong> We live and breath internet marketing and work with clients across all their online marketing, just like their own in-house consultant.</li>
      <li><strong>Remain Competitive:</strong> You have a business to run. We ensure you stay ahead of competitors by focusing on your marketing while you focus on your business.</li>
      <li><strong>Personal Service:</strong> The only way to really get to know our clients &amp; their business is in person, we do this with regular visits &amp; even the occasional beer.</li>
      <li><strong>Not Another Sales Pitch:</strong> We know businesses are tired of being sold the next best thing. Bright Path ensures you are always using the latest technology &amp; strategies available to smash competitors and grow your business.</li>
    </ul>
  </aside>

  <footer class="site-footer">
    <nav class="footer-nav">
      <a href="#" class="active">Home</a><span class="sep">|</span><a href="#">Services</a><span class="sep">|</span><a href="#">About Us</a><span class="sep">|</span><a href="#">Blog</a><span class="sep">|</span><a href="#">Contact Us</a>
    </nav>
    <div class="badge cert" role="img" aria-label="Advertising certification badge"></div>
    <div class="badge assoc" role="img" aria-label="Web industry association membership badge"></div>
  </footer>
</body>
</html>
```